Creative pkg design 4 our craft cannabis vaporizer cartridges that stands out above the so-so boxes

We need a package design for our full spectrum terpene rich vaporizer cannabis cartridges that complies with DVRB regulations and conveys a modern, colorful, clean, natural feel to a youngish market. Our cannabis is from the northwest (USA) where we appreciate the clean air, mountains, rivers and healthiness of the area. We stress quality, purity & sustainability. Our marijuana farm is also a trout farm and our logo uses triangles to symbolize the mountains. We are printing on a white box and like this as a foundation. Our logo is usually either silver and black (text silver or black with background opposite) but we are open to playing with the colors & affects etc. We want our package to pop and stand out from the rest. Our market is obviously marijuana users that are over 21, somewhat sophisticated and focused on value and quality from an experienced, trustworthy company. The DVRB requires special placement of some text and some symbols. See layout file. There is a lot of text required but we're hoping for a cool image or graphic concept incorporated behind or dispersed throughout. Our company is Copper Meadow Distillates (CMD)
Updates

We are extending the deadline until next Wednesday. We updated the brief and are looking for something a little more creative and colorful. Not quite so serious and conservative

Target Market(s)

marijuana users over 21, somewhat sophisticated, healthy and focused on value and quality from an experienced, trustworthy company

Industry/Entity Type

Cannabis - marijuana

Font styles to use
Sans Serif

Requirements
Must have
• Must have required text as stated in layout attachment
Should not have
• Cannot be cartoonish

```html
<!DOCTYPE html>
<html lang="en">
<head>
<meta charset="utf-8">
<title>Copper Meadow Distillates – Cartridge Boxes</title>
<link rel="stylesheet" href="https://fonts.googleapis.com/css2?family=Poppins:wght@400;500;600;900&family=Saira+Semi+Condensed:wght@600&family=Roboto+Mono:wght@600&display=swap">
<style>
  :root{
    --page:#c9c1c2;
    --white:#ffffff;
    --ink:#111111;
    --warn-red:#d8161b;
    --slate-dark:#3f5270; --slate-light:#7596c4;
    --mint-dark:#08d070;  --mint-light:#54eea6;
    --plum-dark:#2f2350;  --plum-light:#7a55bf;
    --copper-dark:#c0703a;--copper-light:#eca66c;
  }
  *{box-sizing:border-box;margin:0;padding:0}
  html,body{width:1200px;height:1200px;overflow:hidden}
  body{background:var(--page);font-family:"Poppins",sans-serif;display:flex;align-items:center;justify-content:center}
  .lineup{display:flex;gap:22px}
  .box{display:flex;width:270px;height:520px;box-shadow:0 10px 24px rgba(0,0,0,.18)}
  .box--slate{--dark:var(--slate-dark);--light:var(--slate-light)}
  .box--mint{--dark:var(--mint-dark);--light:var(--mint-light)}
  .box--plum{--dark:var(--plum-dark);--light:var(--plum-light)}
  .box--copper{--dark:var(--copper-dark);--light:var(--copper-light)}

  /* side panel */
  .side{width:80px;display:flex;flex-direction:column;background:linear-gradient(90deg,#e6e6e6,var(--white));border-right:1px solid rgba(0,0,0,.08)}
  .side__band{height:78px;background:var(--dark);display:flex;align-items:center;justify-content:center}
  .side__mark{width:26px;height:26px;border:1.5px solid var(--white);border-radius:50%}
  .side__story{padding:8px 6px 0;font-size:6px;line-height:1.35;color:var(--ink)}
  .side__story h3{font-size:6.6px;font-weight:600}
  .side__story p{margin-top:5px}
  .side__handles{margin-top:6px;font-size:4.8px;font-weight:500;line-height:1.5;white-space:nowrap}
  .side__art{flex:1;margin-top:8px;background:linear-gradient(180deg,var(--light),var(--dark) 75%)}
  .side__warning{height:104px;background:var(--dark);color:var(--white);font-size:5.8px;line-height:1.4;padding:8px 6px}
  .side__warning-icon{display:block;width:10px;margin:0 auto 4px}

  /* front panel */
  .front{flex:1;display:flex;flex-direction:column;background:linear-gradient(180deg,#e9e9e9,var(--white) 40%,var(--white))}
  .front__band{height:78px;background:var(--dark);color:var(--white);font-family:"Saira Semi Condensed",sans-serif;font-weight:600;font-size:16px;line-height:1.1;letter-spacing:.5px;text-align:center;display:flex;align-items:center;justify-content:center}
  .brand{display:flex;flex-direction:column;align-items:center;gap:8px;margin-top:26px}
  .brand__circle{width:70px;height:70px;border:3px solid var(--dark);border-radius:50%}
  .brand__name{font-size:10px;font-weight:600;letter-spacing:1.5px;text-transform:uppercase;color:var(--dark)}
  .front__type{margin-top:30px;text-align:center;font-size:8.6px;color:var(--ink)}
  .front__strain{margin-top:4px;text-align:center;font-weight:900;font-size:24px;line-height:.98;color:var(--dark);text-transform:uppercase;height:52px}
  .front__art{flex:1;background:linear-gradient(180deg,var(--white),var(--light) 45%,var(--dark))}
  .front__facts{height:104px;background:var(--dark);color:var(--white);padding:12px 10px 8px;display:grid;grid-template-columns:64px 1fr;grid-template-rows:1fr auto;column-gap:8px}
  .warn-symbol{width:64px;height:48px;background:var(--ink);border-radius:5px;display:flex;padding:4px;gap:3px}
  .warn-symbol__bang{width:14px;background:var(--white);border-radius:2px}
  .warn-symbol__field{flex:1;background:var(--warn-red);border-radius:2px}
  .potency{font-family:"Roboto Mono",monospace;font-size:6.4px;font-weight:600}
  .potency__row{display:flex;justify-content:space-between;gap:4px;border-bottom:1px solid rgba(255,255,255,.8);padding:3px 0;white-space:nowrap}
  .potency__row:last-child{border-bottom:none}
  .net-weight{grid-column:1/3;text-align:center;font-family:"Roboto Mono",monospace;font-size:7.4px;font-weight:600;letter-spacing:.3px}
</style>
</head>
<body>
<main class="lineup">

  <article class="box box--slate">
    <section class="side">
      <div class="side__band"><span class="side__mark"></span></div>
      <div class="side__story">
        <h3>Our story</h3>
        <p>We raise small-batch cannabis beside a cold spring creek in the Cascade foothills. Every oil is refined in limited runs and stays fully plant derived.</p>
        <p>We're neighbors who care for the land, clean water and honest farming. Our creek-fed fields keep our footprint light on local resources.</p>
        <p>CMD oils are whole plant with nothing added.</p>
        <p>Taste the valley in every pull!</p>
        <div class="side__handles">@coppermeadowdistillates<br>@coppermeadowfarms</div>
      </div>
      <div class="side__art" role="img" aria-label="Mountain peak and pine forest illustration"></div>
      <div class="side__warning">
        <svg class="side__warning-icon" viewBox="0 0 10 9"><path d="M5 .5L9.5 8.5H.5Z" fill="none" stroke="#fff" stroke-width=".8"/><path d="M5 3.2v2.6M5 6.6v.6" stroke="#fff" stroke-width=".8"/></svg>
        This package is not child resistant. This product is not approved by the FDA to treat, cure or prevent any disease.
      </div>
    </section>
    <section class="front">
      <div class="front__band">CANNABIS EXTRACT<br>CARTRIDGE</div>
      <div class="brand"><span class="brand__circle"></span><span class="brand__name">Copper Meadow Farms</span></div>
      <p class="front__type">Cannabis Derived Terpenes + Distillate</p>
      <h2 class="front__strain">Summit<br>Cookies</h2>
      <div class="front__art" role="img" aria-label="Mountain range and pine forest illustration"></div>
      <div class="front__facts">
        <div class="warn-symbol" role="img" aria-label="Required cannabis warning symbol"><span class="warn-symbol__bang"></span><span class="warn-symbol__field"></span></div>
        <div class="potency">
          <div class="potency__row"><span>THC: xx%</span><span>CBD: xx%</span></div>
          <div class="potency__row"><span>Terpenes:</span><span>xx%</span></div>
          <div class="potency__row"><span>Total Cannabinoids:</span><span>xx%</span></div>
        </div>
        <p class="net-weight">NET WEIGHT : 1G (0.035 OZ)</p>
      </div>
    </section>
  </article>

  <article class="box box--mint">
    <section class="side">
      <div class="side__band"><span class="side__mark"></span></div>
      <div class="side__story">
        <h3>Our story</h3>
        <p>We raise small-batch cannabis beside a cold spring creek in the Cascade foothills. Every oil is refined in limited runs and stays fully plant derived.</p>
        <p>We're neighbors who care for the land, clean water and honest farming. Our creek-fed fields keep our footprint light on local resources.</p>
        <p>CMD oils are whole plant with nothing added.</p>
        <p>Taste the valley in every pull!</p>
        <div class="side__handles">@coppermeadowdistillates<br>@coppermeadowfarms</div>
      </div>
      <div class="side__art" role="img" aria-label="Mountain peak and pine forest illustration"></div>
      <div class="side__warning">
        <svg class="side__warning-icon" viewBox="0 0 10 9"><path d="M5 .5L9.5 8.5H.5Z" fill="none" stroke="#fff" stroke-width=".8"/><path d="M5 3.2v2.6M5 6.6v.6" stroke="#fff" stroke-width=".8"/></svg>
        This package is not child resistant. This product is not approved by the FDA to treat, cure or prevent any disease.
      </div>
    </section>
    <section class="front">
      <div class="front__band">CANNABIS EXTRACT<br>CARTRIDGE</div>
      <div class="brand"><span class="brand__circle"></span><span class="brand__name">Copper Meadow Farms</span></div>
      <p class="front__type">Cannabis Derived Terpenes + Distillate</p>
      <h2 class="front__strain">Canyon 27</h2>
      <div class="front__art" role="img" aria-label="Mountain range and pine forest illustration"></div>
      <div class="front__facts">
        <div class="warn-symbol" role="img" aria-label="Required cannabis warning symbol"><span class="warn-symbol__bang"></span><span class="warn-symbol__field"></span></div>
        <div class="potency">
          <div class="potency__row"><span>THC: xx%</span><span>CBD: xx%</span></div>
          <div class="potency__row"><span>Terpenes:</span><span>xx%</span></div>
          <div class="potency__row"><span>Total Cannabinoids:</span><span>xx%</span></div>
        </div>
        <p class="net-weight">NET WEIGHT : 1G (0.035 OZ)</p>
      </div>
    </section>
  </article>

  <article class="box box--plum">
    <section class="side">
      <div class="side__band"><span class="side__mark"></span></div>
      <div class="side__story">
        <h3>Our story</h3>
        <p>We raise small-batch cannabis beside a cold spring creek in the Cascade foothills. Every oil is refined in limited runs and stays fully plant derived.</p>
        <p>We're neighbors who care for the land, clean water and honest farming. Our creek-fed fields keep our footprint light on local resources.</p>
        <p>CMD oils are whole plant with nothing added.</p>
        <p>Taste the valley in every pull!</p>
        <div class="side__handles">@coppermeadowdistillates<br>@coppermeadowfarms</div>
      </div>
      <div class="side__art" role="img" aria-label="Mountain peak and pine forest illustration"></div>
      <div class="side__warning">
        <svg class="side__warning-icon" viewBox="0 0 10 9"><path d="M5 .5L9.5 8.5H.5Z" fill="none" stroke="#fff" stroke-width=".8"/><path d="M5 3.2v2.6M5 6.6v.6" stroke="#fff" stroke-width=".8"/></svg>
        This package is not child resistant. This product is not approved by the FDA to treat, cure or prevent any disease.
      </div>
    </section>
    <section class="front">
      <div class="front__band">CANNABIS EXTRACT<br>CARTRIDGE</div>
      <div class="brand"><span class="brand__circle"></span><span class="brand__name">Copper Meadow Farms</span></div>
      <p class="front__type">Cannabis Derived Terpenes + Distillate</p>
      <h2 class="front__strain">Violet<br>Peach</h2>
      <div class="front__art" role="img" aria-label="Mountain range and pine forest illustration"></div>
      <div class="front__facts">
        <div class="warn-symbol" role="img" aria-label="Required cannabis warning symbol"><span class="warn-symbol__bang"></span><span class="warn-symbol__field"></span></div>
        <div class="potency">
          <div class="potency__row"><span>THC: xx%</span><span>CBD: xx%</span></div>
          <div class="potency__row"><span>Terpenes:</span><span>xx%</span></div>
          <div class="potency__row"><span>Total Cannabinoids:</span><span>xx%</span></div>
        </div>
        <p class="net-weight">NET WEIGHT : 1G (0.035 OZ)</p>
      </div>
    </section>
  </article>

  <article class="box box--copper">
    <section class="side">
      <div class="side__band"><span class="side__mark"></span></div>
      <div class="side__story">
        <h3>Our story</h3>
        <p>We raise small-batch cannabis beside a cold spring creek in the Cascade foothills. Every oil is refined in limited runs and stays fully plant derived.</p>
        <p>We're neighbors who care for the land, clean water and honest farming. Our creek-fed fields keep our footprint light on local resources.</p>
        <p>CMD oils are whole plant with nothing added.</p>
        <p>Taste the valley in every pull!</p>
        <div class="side__handles">@coppermeadowdistillates<br>@coppermeadowfarms</div>
      </div>
      <div class="side__art" role="img" aria-label="Mountain peak and pine forest illustration"></div>
      <div class="side__warning">
        <svg class="side__warning-icon" viewBox="0 0 10 9"><path d="M5 .5L9.5 8.5H.5Z" fill="none" stroke="#fff" stroke-width=".8"/><path d="M5 3.2v2.6M5 6.6v.6" stroke="#fff" stroke-width=".8"/></svg>
        This package is not child resistant. This product is not approved by the FDA to treat, cure or prevent any disease.
      </div>
    </section>
    <section class="front">
      <div class="front__band">CANNABIS EXTRACT<br>CARTRIDGE</div>
      <div class="brand"><span class="brand__circle"></span><span class="brand__name">Copper Meadow Farms</span></div>
      <p class="front__type">Cannabis Derived Terpenes + Distillate</p>
      <h2 class="front__strain">Sugared<br>Cruller</h2>
      <div class="front__art" role="img" aria-label="Mountain range and pine forest illustration"></div>
      <div class="front__facts">
        <div class="warn-symbol" role="img" aria-label="Required cannabis warning symbol"><span class="warn-symbol__bang"></span><span class="warn-symbol__field"></span></div>
        <div class="potency">
          <div class="potency__row"><span>THC: xx%</span><span>CBD: xx%</span></div>
          <div class="potency__row"><span>Terpenes:</span><span>xx%</span></div>
          <div class="potency__row"><span>Total Cannabinoids:</span><span>xx%</span></div>
        </div>
        <p class="net-weight">NET WEIGHT : 1G (0.035 OZ)</p>
      </div>
    </section>
  </article>

</main>
</body>
</html>
```